Fern Guildworks Business Cards

Looking or a business card design for my start-up, called "Fern Guildworks".
Our tagline is "Unleashing the human potential for good through leadership, culture, and education."
Our mission-driven work includes professional/personal development workshops, educational design services, organizational & project management consulting, and coaching services for K-12 schools, organizations, and individuals.
You can check out the website we're building at fernguildworks.com
I select projects from designers who are highly responsive to feedback, engage in dialog about revisions, and provide all root/source documents (so please state in your initial submission that you agree to do so).
Looking forward to seeing your great designs!!
Updates
Hello everyone,
Industry/Entity Type
Building
Requirements
Must have
- Looking for a two sided design that includes our logo (I am uploading two variations that I would like incorporated in .ai format) and website on both sides.
The front side must include:
Logo, Name, Title, Phone, Email, Twitter handle
The back side must include: Logo, @ferngild (our organizational twitter handle)
Nice to have
- I like the rounded corner business cards, but that is not absolutely essential.
Should not have
- Colors beyond those presented in our logo.

```html
<!DOCTYPE html>
<html lang="en">
<head>
<meta charset="utf-8">
<title>Fern Guildworks Business Cards</title>
<link href="https://fonts.googleapis.com/css2?family=Tinos:wght@400&display=swap" rel="stylesheet">
<style>
  :root {
    --sky: #66c7e1;
    --sky-deep: #58b8d3;
    --stone: #a9a39e;
    --white: #ffffff;
    --paper: #e7e3dc;
    --ink-soft: #8f8a85;
  }
  * { margin: 0; padding: 0; box-sizing: border-box; }
  html, body { width: 1200px; height: 900px; overflow: hidden; }
  body {
    background: var(--paper);
    font-family: "Tinos", "Times New Roman", serif;
    position: relative;
  }
  .card {
    position: absolute;
    top: 290px;
    width: 560px;
    height: 320px;
    border-radius: 26px;
    overflow: hidden;
    box-shadow: 0 6px 18px rgba(0,0,0,0.18);
  }
  /* Back side */
  .card-back { left: 20px; background: var(--sky); color: var(--white); }
  .card-back .brand { position: absolute; top: 72px; left: 0; right: 0; display: flex; align-items: center; justify-content: center; gap: 16px; }
  .brand-dot { width: 46px; height: 46px; border-radius: 50%; }
  .card-back .brand-dot { background: var(--white); }
  .brand-name { font-size: 34px; letter-spacing: 1px; text-transform: uppercase; line-height: 1; }
  .pillars { font-size: 11px; letter-spacing: 4px; text-transform: uppercase; text-align: center; }
  .card-back .pillars { position: absolute; top: 136px; left: 0; right: 0; }
  .tagline { position: absolute; top: 172px; left: 0; right: 0; text-align: center; font-size: 13px; letter-spacing: 1.5px; text-transform: uppercase; line-height: 1.5; }
  .card-back .site { position: absolute; top: 240px; left: 0; right: 0; text-align: center; font-size: 17px; }

  /* Front side */
  .card-front { left: 620px; background: var(--white); }
  .contact-band { position: absolute; top: 0; right: 0; width: 260px; height: 92px; background: var(--sky-deep); color: var(--white); padding: 14px 0 0 26px; }
  .contact-line { display: flex; align-items: center; gap: 8px; font-size: 14px; line-height: 21px; }
  .contact-line svg { width: 14px; height: 14px; flex: none; }
  .card-front .brand { position: absolute; top: 128px; left: 0; right: 0; display: flex; align-items: center; justify-content: center; gap: 16px; color: var(--stone); }
  .card-front .brand-dot { background: var(--sky); }
  .card-front .pillars { position: absolute; top: 186px; left: 0; right: 0; color: var(--ink-soft); }
  .name-band { position: absolute; left: 0; bottom: 0; width: 330px; height: 82px; background: var(--sky); color: var(--white); padding: 12px 0 0 28px; }
  .name-band::before { content: ""; position: absolute; left: 22px; top: -12px; border-left: 12px solid transparent; border-right: 12px solid transparent; border-bottom: 12px solid var(--sky); }
  .person { font-size: 17px; text-transform: uppercase; letter-spacing: 1px; }
  .role { font-size: 14px; margin-top: 2px; }
  .name-band .site { font-size: 14px; margin-top: 4px; }
</style>
</head>
<body>
  <section class="card card-back" aria-label="Card back">
    <div class="brand"><span class="brand-dot"></span><span class="brand-name">Fern Guildworks</span></div>
    <p class="pillars">Leadership | Culture | Education</p>
    <p class="tagline">Unleashing the human potential for good through<br>leadership, culture, and education</p>
    <p class="site">www.fernguildworks.com</p>
  </section>

  <section class="card card-front" aria-label="Card front">
    <div class="contact-band">
      <p class="contact-line">
        <svg viewBox="0 0 14 14"><circle cx="7" cy="7" r="6.3" fill="none" stroke="#fff" stroke-width="1.2"/><path d="M4.6 3.8l1.3 1.4-.7.9c.5 1 1.3 1.8 2.3 2.3l.9-.7 1.4 1.3-.8 1.1C6.8 9.8 4.2 7.2 3.9 4.6z" fill="#fff"/></svg>
        000 000 000
      </p>
      <p class="contact-line">
        <svg viewBox="0 0 14 14"><circle cx="7" cy="7" r="6.3" fill="none" stroke="#fff" stroke-width="1.2"/><rect x="3.8" y="4.8" width="6.4" height="4.4" fill="none" stroke="#fff" stroke-width="1"/><path d="M3.8 4.8L7 7.4l3.2-2.6" fill="none" stroke="#fff" stroke-width="1"/></svg>
        name@domainname.com
      </p>
      <p class="contact-line">
        <svg viewBox="0 0 14 14"><circle cx="7" cy="7" r="6.3" fill="none" stroke="#fff" stroke-width="1.2"/><circle cx="7" cy="7" r="2.4" fill="#fff"/></svg>
        @ferngild
      </p>
    </div>
    <div class="brand"><span class="brand-dot"></span><span class="brand-name">Fern Guildworks</span></div>
    <p class="pillars">Leadership | Culture | Education</p>
    <div class="name-band">
      <p class="person">Your Name</p>
      <p class="role">Job Title</p>
      <p class="site">www.fernguildworks.com</p>
    </div>
  </section>
</body>
</html>
```